Fern Hollow Academy business card

we need to incorporate our school logo, name, address onto a great new school business card for all our staff - I included a lot of detail below under must haves and I included 3 business card samples below also that give a flavour of what I want - I would like to include a great graphic on at least one side of the card that represents education -

Target Market(s)

this business card will need to be attractive to parents of all ages but especially millennial parents and even high school students who may influence parents to chose Fern Hollow Academy

Industry/Entity Type

Education

Contact Information for Business Card

should contain core value words "excellence service family belief"
will need out school name, Fern Hollow Academy to be present, address 7281 Marston Avenue, Burnaby, British Columbia V3K8P1
telephone 604.871.2960 Ext. 317
first card will need my name on it, Maribel Tansey, Director of Development & Operations
also web address of fernhollowacademy.ca

Font styles to use
Other font styles liked:
• Tw Cent MT

Requirements
Must have
• a fresh modern look for a private school environment that appeals to parents looking for great education - must use school logo, and incorporate colours navy blue, CMYK 100, 60, 0, 56 and burgundy CMYK 27, 98, 81, 50
• below I uploaded 3 business card layouts that look interesting to me - I'd like to incorporate some great school photos into the design - I tried to upload some school photos that we have, that the files are too large apparently? so I could send a link to Filecrate or something like that to share great high res pics that would look nice - we are kindergarten to Gr. 12 school, so I would like to include images that would represent great education at any age.
Nice to have
• spot colour would be nice as an option for printing for maybe key administrator business cards, while the rest would be basic printing

```html
<!DOCTYPE html>
<html lang="en">
<head>
<meta charset="utf-8">
<title>Fern Hollow Academy – Business Card</title>
<link rel="stylesheet" href="https://fonts.googleapis.com/css2?family=Archivo:ital,wght@0,400;0,700;0,800;1,800&display=swap">
<style>
  :root {
    --navy: #002d70;
    --navy-deep: #0a1f52;
    --burgundy: #6e0d1f;
    --burgundy-bright: #8c1526;
    --orange: #e0481f;
    --orange-light: #f06a2c;
    --white: #ffffff;
    --ground: #e6e6e4;
    --ink-soft: rgba(255,255,255,0.85);
  }
  * { margin: 0; padding: 0; box-sizing: border-box; }
  html, body {
    width: 1200px; height: 696px; overflow: hidden;
    background: var(--ground);
    font-family: "Archivo", Arial, sans-serif;
  }
  .sheet {
    position: relative; width: 1200px; height: 696px;
    display: flex; align-items: center; justify-content: center; gap: 40px;
  }
  .card {
    position: relative; width: 540px; height: 309px; overflow: hidden;
    background: var(--white);
    box-shadow: 0 6px 18px rgba(0,0,0,0.18);
  }
  .card-art { position: absolute; inset: 0; width: 100%; height: 100%; }

  /* Front */
  .school-mark {
    position: absolute; left: 30px; top: 30px;
    display: flex; align-items: center; gap: 10px;
  }
  .school-mark__dot {
    width: 34px; height: 34px; border-radius: 50%; background: var(--navy);
  }
  .school-mark__name {
    font-weight: 800; font-size: 19px; line-height: 1; color: var(--burgundy);
    text-transform: uppercase; letter-spacing: 0.5px; width: 130px;
  }
  .core-values {
    position: absolute; right: 30px; top: 46px; text-align: right;
    font-weight: 800; font-style: italic; font-size: 15px; line-height: 1.35;
    letter-spacing: 0.4px; text-transform: uppercase;
  }
  .core-values__primary { color: var(--burgundy); }
  .core-values__secondary { color: var(--navy); }

  /* Back */
  .contact {
    position: absolute; left: 32px; top: 190px; right: 40px; color: var(--white);
  }
  .contact__name { font-weight: 700; font-size: 18px; }
  .contact__title { font-size: 10.5px; margin-top: 2px; color: var(--ink-soft); }
  .contact__school { font-weight: 700; font-size: 10.5px; margin-top: 14px; }
  .contact__address { font-size: 10.5px; margin-top: 2px; padding-bottom: 6px;
    border-bottom: 1px solid rgba(255,255,255,0.6); width: 330px; }
  .contact__lines { font-size: 10.5px; margin-top: 6px; }
</style>
</head>
<body>
<main class="sheet">

  <!-- Front of card -->
  <section class="card card--front" aria-label="Card front">
    <svg class="card-art" viewBox="0 0 540 309" preserveAspectRatio="none">
      <defs>
        <linearGradient id="frontWarm" x1="0" y1="0" x2="1" y2="0.3">
          <stop offset="0" stop-color="var(--orange-light)"/>
          <stop offset="1" stop-color="var(--orange)"/>
        </linearGradient>
        <radialGradient id="activityGlow" cx="0.5" cy="0.5" r="0.6">
          <stop offset="0" stop-color="#f7d9c9"/>
          <stop offset="1" stop-color="#e65a25" stop-opacity="0"/>
        </radialGradient>
      </defs>
      <rect width="540" height="309" fill="url(#frontWarm)"/>
      <path d="M0 110 C120 95 230 115 330 160 C420 200 480 215 540 222 L540 0 L0 0 Z" fill="var(--navy)"/>
      <path d="M0 102 C130 88 240 108 340 150 C420 184 470 195 540 200 L540 0 L0 0 Z" fill="var(--white)"/>
      <path d="M330 158 C400 185 470 198 540 204 L540 198 C470 192 410 178 350 160 Z" fill="var(--burgundy)"/>
      <g role="img" aria-label="Photo of students performing a dance lift">
        <rect x="20" y="120" width="160" height="189" fill="url(#activityGlow)"/>
      </g>
    </svg>
    <div class="school-mark">
      <span class="school-mark__dot"></span>
      <span class="school-mark__name">Fern Hollow Academy</span>
    </div>
    <div class="core-values">
      <div class="core-values__primary">Excellence Service</div>
      <div class="core-values__secondary">Family Belief</div>
    </div>
  </section>

  <!-- Back of card -->
  <section class="card card--back" aria-label="Card back">
    <svg class="card-art" viewBox="0 0 540 309" preserveAspectRatio="none">
      <defs>
        <linearGradient id="gradPhoto" x1="0" y1="0" x2="1" y2="0">
          <stop offset="0" stop-color="#7a6a62"/>
          <stop offset="0.45" stop-color="#3a2a26"/>
          <stop offset="1" stop-color="#141418"/>
        </linearGradient>
      </defs>
      <rect width="540" height="309" fill="var(--navy-deep)"/>
      <g role="img" aria-label="Photo of graduating students in caps and gowns">
        <rect width="540" height="180" fill="url(#gradPhoto)"/>
      </g>
      <path d="M0 180 C150 175 330 150 540 100 L540 309 L0 309 Z" fill="var(--navy)"/>
      <path d="M0 160 C160 160 330 130 540 80 L540 140 C350 168 170 178 0 182 Z" fill="var(--burgundy)"/>
      <path d="M0 182 C170 178 350 168 540 140 L540 146 C350 174 170 184 0 188 Z" fill="var(--burgundy-bright)"/>
    </svg>
    <div class="contact">
      <div class="contact__name">Maribel Tansey</div>
      <div class="contact__title">Director of Development &amp; Operations</div>
      <div class="contact__school">Fern Hollow Academy</div>
      <div class="contact__address">7281 Marston Avenue, Burnaby, British Columbia V3K8P1</div>
      <div class="contact__lines">T: 604.871.2960 Ext. 317 &nbsp;|&nbsp; W: fernhollowacademy.ca</div>
    </div>
  </section>

</main>
</body>
</html>
```